Satchel & Compass needs new business card design

I need a new business card design. I'm looking for out-of-the-box design which represents the freedom of being a location independent entrepreneur.
I offer coaching, retreats and trips.
I would like to see designs with and without the photo.
Colors I use are black (#000000), green (#25A796) and brown (#D7C38C)
Website satchelandcompass.com

Target Market(s)

location independent entrepreneurs, digital nomads, people looking to swap the 9 to 5 for a lifestyle business

Industry/Entity Type

Business

Contact Information for Business Card

Petra Varga
Your Lifestyle Business Coach, Retreat & Trip Leader
http://satchelandcompass.com
hello@satchelandcompass.com
Live a life you don't need a holiday from

Font styles to use
Serif
Sans Serif

Requirements
Must have
• One side should contain only the logo. I would also consider having the "Live a life you don't need a holiday from" on that side too (depending on how it looks)
• Please show both sides on the designs.

```html
<!DOCTYPE html>
<html lang="en">
<head>
<meta charset="utf-8">
<title>Satchel &amp; Compass — Business Card</title>
<link rel="stylesheet" href="https://fonts.googleapis.com/css2?family=Archivo:ital,wght@0,400;0,600;0,700;1,400&display=swap">
<style>
  :root {
    --backdrop: #3d342f;
    --card: #141414;
    --card-edge: #1d1d1d;
    --brand-green: #25a796;
    --silver: #a9a9a9;
    --white: #f4f4f4;
    --muted: #8c8c8c;
    --divider: #6a6a6a;
  }
  * { margin: 0; padding: 0; box-sizing: border-box; }
  html, body {
    width: 1200px;
    height: 864px;
    overflow: hidden;
    background: var(--backdrop);
    font-family: "Archivo", Arial, sans-serif;
  }
  .sheet {
    width: 1200px;
    height: 864px;
    display: flex;
    flex-direction: column;
    align-items: center;
    justify-content: center;
    gap: 56px;
  }
  .card {
    position: relative;
    width: 620px;
    height: 354px;
    background: var(--card);
    border: 1px solid var(--card-edge);
    box-shadow: 0 10px 28px rgba(0, 0, 0, 0.45);
  }

  /* Logo side */
  .card--logo .wordmark {
    position: absolute;
    left: 150px;
    top: 118px;
    font-weight: 700;
    font-size: 34px;
    letter-spacing: 1px;
    text-transform: uppercase;
    color: var(--silver);
  }
  .card--logo .motto {
    position: absolute;
    left: 70px;
    top: 236px;
    font-style: italic;
    font-size: 15px;
    color: var(--muted);
  }
  .social {
    position: absolute;
    top: 40px;
    right: 42px;
    display: flex;
    gap: 5px;
  }
  .social span {
    width: 18px;
    height: 18px;
    background: var(--brand-green);
  }

  /* Contact side */
  .card--contact .wordmark {
    position: absolute;
    left: 40px;
    top: 150px;
    width: 250px;
    font-weight: 700;
    font-size: 25px;
    line-height: 1.15;
    letter-spacing: 0.5px;
    text-transform: uppercase;
    color: var(--white);
  }
  .card--contact .rule {
    position: absolute;
    left: 304px;
    top: 112px;
    width: 1px;
    height: 150px;
    background: var(--divider);
  }
  .details {
    position: absolute;
    left: 326px;
    top: 124px;
    color: var(--white);
  }
  .details .name {
    font-weight: 600;
    font-size: 20px;
    color: var(--brand-green);
    margin-bottom: 4px;
  }
  .details .role {
    font-size: 16px;
    line-height: 1.3;
    margin-bottom: 14px;
  }
  .details .line {
    display: flex;
    align-items: center;
    gap: 10px;
    font-size: 14px;
    line-height: 1.6;
  }
  .details .line svg { flex: none; }
</style>
</head>
<body>
  <main class="sheet">
    <section class="card card--logo" aria-label="Business card, logo side">
      <div class="social" aria-label="Social profiles">
        <span></span><span></span><span></span>
      </div>
      <div class="wordmark">Satchel &amp; Compass</div>
      <p class="motto">Live a life you don't need a holiday from</p>
    </section>

    <section class="card card--contact" aria-label="Business card, contact side">
      <div class="wordmark">Satchel &amp; Compass</div>
      <div class="rule"></div>
      <div class="details">
        <p class="name">Petra Varga</p>
        <p class="role">Your Lifestyle Business Coach<br>Retreat &amp; Trip Leader</p>
        <p class="line">
          <svg width="14" height="11" viewBox="0 0 14 11" aria-hidden="true">
            <rect x="0.5" y="0.5" width="13" height="10" rx="1" fill="var(--brand-green)"/>
            <path d="M1 1.5 L7 6 L13 1.5" fill="none" stroke="var(--card)" stroke-width="1.3"/>
          </svg>
          hello@satchelandcompass.com
        </p>
        <p class="line">
          <svg width="14" height="14" viewBox="0 0 14 14" aria-hidden="true">
            <circle cx="7" cy="7" r="7" fill="var(--brand-green)"/>
            <circle cx="7" cy="5.2" r="2.2" fill="var(--card)"/>
            <path d="M3 11.2 C4 8.8 10 8.8 11 11.2" fill="var(--card)"/>
          </svg>
          www.satchelandcompass.com
        </p>
      </div>
    </section>
  </main>
</body>
</html>
```